Package for a Mouthfreshener called ZOLV!!

We are looking for an awesome packaging design for a bran new product called “Zolv Mouthfreshener”

This product is going to be made in USA so is really importar that ‘Made in USA” is part of the packaging.

We also need to include the ingredients that are going to be the following:
Saffron
cardamom
menthol
catechu
permited spices and falvors
tree nuts.

We are looking to haver this in a green or purple color and to clarify that the “best before” is for 2 years after the production date

Target Market(s)

Indian stores in usa

Colors
0094D4
00A9DD
6FCCEA
C7EBF8
E9F6FB
00AB8E
00BBA5
67D7C9
C6EFE9
E9F9F6
6B429C
8869AF
B7A5CE
E3DAEB
F3F0F8

Requirements
Must have
• Ingredients
Nice to have
• A good font and is important to mention is made in USA on images I upload an idea for the font

```html
<!DOCTYPE html>
<html lang="en">
<head>
<meta charset="utf-8">
<title>Zolv Mouthfreshener – Sachet Front</title>
<link href="https://fonts.googleapis.com/css2?family=Montserrat:wght@800;900&family=Permanent+Marker&family=Caveat:wght@700&display=swap" rel="stylesheet">
<style>
  :root {
    --teal: #19ab92;
    --teal-light: #3fbda7;
    --teal-deep: #128a76;
    --forest: #0d4a3f;
    --white: #ffffff;
    --paper: #f4f6f5;
    --flag-blue: #24306e;
    --flag-red: #c21f2a;
  }
  * { margin: 0; padding: 0; box-sizing: border-box; }
  html, body {
    width: 1071px;
    height: 1200px;
    overflow: hidden;
    background: var(--white);
  }
  .canvas {
    position: relative;
    width: 1071px;
    height: 1200px;
  }
  .sachet {
    position: absolute;
    left: 128px;
    top: 100px;
    width: 814px;
    height: 1000px;
    background: var(--teal);
    overflow: hidden;
    font-family: "Montserrat", Arial, sans-serif;
  }
  .sachet__bands {
    position: absolute;
    inset: 0;
    width: 100%;
    height: 100%;
  }
  .sachet__seal {
    position: absolute;
    left: 0;
    width: 100%;
    height: 18px;
    background: repeating-linear-gradient(90deg, var(--teal-deep) 0 2px, var(--teal) 2px 7px);
    opacity: 0.55;
  }
  .sachet__seal--top { top: 0; }
  .sachet__seal--bottom { bottom: 0; }
  .flag-mark {
    position: absolute;
    left: 222px;
    top: 101px;
    width: 371px;
    height: 75px;
    background: linear-gradient(90deg, var(--flag-blue) 0 48%, var(--flag-red) 48% 75%, #d9d9d9 75%);
    clip-path: polygon(0 12%, 100% 20%, 96% 70%, 40% 82%, 2% 100%);
  }
  .origin {
    position: absolute;
    left: 0;
    width: 100%;
    top: 183px;
    text-align: center;
    font-weight: 800;
    font-size: 34px;
    color: var(--forest);
    letter-spacing: 1px;
  }
  .brand-name {
    position: absolute;
    left: 0;
    width: 100%;
    top: 255px;
    text-align: center;
    font-weight: 900;
    font-size: 230px;
    line-height: 1;
    color: var(--white);
    letter-spacing: 4px;
  }
  .product-type {
    position: absolute;
    left: 0;
    width: 100%;
    top: 578px;
    text-align: center;
    font-family: "Permanent Marker", "Comic Sans MS", cursive;
    font-size: 62px;
    line-height: 1.1;
    color: var(--forest);
    text-transform: uppercase;
  }
  .ingredients {
    position: absolute;
    left: 84px;
    top: 667px;
    width: 639px;
    height: 225px;
    background: var(--paper);
    clip-path: polygon(1% 4%, 30% 0, 70% 2%, 99% 0, 100% 40%, 98% 100%, 60% 97%, 20% 100%, 0 96%, 2% 50%);
    padding: 30px 22px 0 58px;
    color: var(--forest);
    font-weight: 800;
  }
  .ingredients__line {
    display: flex;
    gap: 30px;
    white-space: nowrap;
  }
  .ingredients__line--major { font-size: 44px; line-height: 52px; }
  .ingredients__line--minor { font-size: 34px; line-height: 46px; margin-top: 4px; }
  .ingredients__note {
    text-align: right;
    font-size: 17px;
    line-height: 18px;
    padding-right: 18px;
  }
  .net-weight {
    position: absolute;
    left: 84px;
    top: 880px;
    width: 422px;
    height: 82px;
    background: linear-gradient(90deg, #1c7a68, var(--forest));
    clip-path: polygon(4% 8%, 97% 0, 100% 60%, 96% 100%, 2% 92%, 0 40%);
    color: var(--white);
    font-weight: 800;
    font-size: 46px;
    line-height: 82px;
    padding-left: 40px;
  }
  .age-limit {
    position: absolute;
    left: 534px;
    top: 908px;
    font-family: "Caveat", cursive;
    font-weight: 700;
    font-size: 68px;
    line-height: 1;
    color: #d8efe9;
  }
</style>
</head>
<body>
  <div class="canvas">
    <div class="sachet">
      <svg class="sachet__bands" viewBox="0 0 814 1000" aria-hidden="true">
        <g fill="var(--teal-light)" opacity="0.45">
          <polygon points="0,120 60,80 140,420 60,470"/>
          <polygon points="600,0 700,0 814,180 814,300"/>
          <polygon points="0,700 90,640 260,1000 160,1000"/>
          <polygon points="660,640 760,600 814,720 814,900 740,940"/>
          <polygon points="380,0 470,0 300,180 240,150"/>
        </g>
      </svg>
      <div class="sachet__seal sachet__seal--top"></div>
      <div class="sachet__seal sachet__seal--bottom"></div>

      <div class="flag-mark" role="img" aria-label="Painted brushstroke of the United States flag"></div>
      <p class="origin">MADE IN USA</p>
      <h1 class="brand-name">ZOLV</h1>
      <p class="product-type">Mouthfreshener</p>

      <div class="ingredients">
        <div class="ingredients__line ingredients__line--major"><span>SAFFRON</span><span>CARDAMOM</span></div>
        <div class="ingredients__line ingredients__line--major"><span>CATECHU</span><span>TREE NUTS.</span></div>
        <div class="ingredients__line ingredients__line--minor"><span>MENTHOL</span><span>PERMITED SPICES</span></div>
        <p class="ingredients__note">AND FLAVORS</p>
      </div>

      <div class="net-weight">NET WT. 5G</div>
      <p class="age-limit">+21</p>
    </div>
  </div>
</body>
</html>
```